Music Business Adviser Needs a Book Cover Design

I need a cover design for my new book called 'The Stage Performer: A Working Handbook for Launching Your Trade'. I am an accountant and tax lawyer specialising in advising international music artists. This book is designed to help music artists and bands navigate through the business world. I would like to see designs that would appeal to young artists, the book needs to be bold and stand out from the crowd, for example it will attract people on Bookvale through its enticing cover.

I am open to you providing creative input on the design, although I like the colour green and think this would perhaps communicate subtly financial safety and growth. The cover should clearly communicate the book is for people in the music industry.

Target Market(s)

Males and females aged between 16 and 30; their hobbies and interest are music; they perform and record music; all genres of music

Industry/Entity Type

Lawyer

Font styles to use
Sans Serif

Requirements
Must have
• Must have the title clearly stated: 'The Stage Performer: A Working Handbook for Launching Your Trade'. It must also have my name as author on the front: 'Gareth L. Quinby'
Nice to have
• I have uploaded an image of the type of artwork, that should be on the book. I like this style - so please keep it simple, not an over complicated design.
Should not have
• Photographs of bands or musicians

```html
<!DOCTYPE html>
<html lang="en">
<head>
<meta charset="utf-8">
<title>The Stage Performer – Book Cover</title>
<link rel="stylesheet" href="https://fonts.googleapis.com/css2?family=Archivo+Black&family=Roboto+Condensed:wght@300;400;700&display=swap">
<style>
  :root {
    --back-green: #04300a;
    --spine-green: #0f4a2b;
    --front-green: #3bb04a;
    --art-green: #0b3d12;
    --gold: #f4b825;
    --rule-red: #b5332a;
    --white: #ffffff;
    --display: "Archivo Black", "Arial Black", sans-serif;
    --condensed: "Roboto Condensed", "Arial Narrow", sans-serif;
  }
  * { margin: 0; padding: 0; box-sizing: border-box; }
  html, body { width: 1200px; height: 885px; overflow: hidden; background: var(--back-green); }
  .cover-spread { position: relative; width: 1200px; height: 885px; overflow: hidden; }

  .back-cover { position: absolute; left: 0; top: 0; width: 586px; height: 885px; background: var(--back-green); }
  .spine { position: absolute; left: 586px; top: 0; width: 27px; height: 885px; background: var(--spine-green); }
  .front-cover { position: absolute; left: 613px; top: 0; width: 587px; height: 885px; background: var(--front-green); }

  .rule { position: absolute; width: 2px; background: var(--rule-red); }

  /* back cover */
  .back-title { position: absolute; left: 210px; top: 80px; color: var(--gold); font-family: var(--display); white-space: nowrap; }
  .back-title .lead { font-size: 37px; letter-spacing: -0.5px; }
  .back-title .tail { font-size: 23px; }
  .back-subtitle { position: absolute; left: 210px; top: 124px; color: var(--white); font-family: var(--condensed); font-weight: 400; font-size: 20px; white-space: nowrap; }
  .back-author { position: absolute; left: 210px; top: 179px; color: var(--white); font-family: var(--condensed); font-weight: 700; font-size: 23px; }
  .blurb { position: absolute; left: 192px; top: 250px; width: 312px; color: var(--white); font-family: var(--condensed); font-weight: 400; font-size: 14.2px; line-height: 24px; text-align: justify; }
  .blurb p + p { margin-top: 24px; }
  .back-motif { position: absolute; left: 0; top: 450px; width: 190px; height: 435px;
    background: radial-gradient(ellipse at 60% 55%, rgba(59,176,74,0.18), rgba(59,176,74,0) 70%); }

  /* spine */
  .spine-text { position: absolute; left: 50%; color: var(--gold); font-family: var(--condensed); font-weight: 700; font-size: 16px; white-space: nowrap; transform-origin: center; }
  .spine-author { top: 126px; transform: translate(-50%, -50%) rotate(90deg); }
  .spine-title { top: 570px; transform: translate(-50%, -50%) rotate(90deg); }

  /* front cover */
  .front-title { position: absolute; left: 118px; top: 96px; color: var(--gold); font-family: var(--display); line-height: 1; white-space: nowrap; }
  .front-title .lead { display: block; font-size: 84px; letter-spacing: -1.5px; }
  .front-title .tail { display: block; font-size: 46px; margin-top: 6px; }
  .front-subtitle { position: absolute; left: 118px; top: 252px; color: var(--white); font-family: var(--condensed); font-weight: 300; font-size: 45px; line-height: 57px; white-space: nowrap; }
  .front-author { position: absolute; left: 118px; top: 752px; color: var(--white); font-family: var(--condensed); font-weight: 700; font-size: 31px; }
  .cover-art { position: absolute; left: 100px; top: 423px; width: 446px; height: 352px; border-radius: 48% 52% 10% 40% / 45% 55% 8% 30%;
    background: radial-gradient(ellipse at 70% 60%, var(--art-green) 0%, rgba(11,61,18,0.75) 45%, rgba(11,61,18,0) 78%); }
</style>
</head>
<body>
<main class="cover-spread">
  <section class="back-cover">
    <div class="rule" style="left:192px; top:0; height:147px;"></div>
    <h2 class="back-title"><span class="lead">the Stage</span> <span class="tail">performer</span></h2>
    <p class="back-subtitle">a working handbook for launching your trade</p>
    <div class="rule" style="left:192px; top:171px; height:42px;"></div>
    <p class="back-author">Gareth L. Quinby</p>

    <div class="blurb">
      <p>The music industry is shapeshifting. Music artists must work harder than ever to make a career of their creative mastery.</p>
      <p>As an artist you are not in a typical profession but you can be big business. A good business mindset starts with ensuring you understand that you are a business and that you will need the right team on board to help you navigate the legal complexities of the business world.</p>
      <p>Whilst you may have a first rate attack in terms of your manager and record label, success won’t be guaranteed unless you have a first rate line of defense to help protect your earnings. This book provides an easy-to-understand overview of setting up in business for the first time, some practical tips on getting started, as well as a discussion of the business challenges you’ll face along your journey to becoming and international superstar.</p>
    </div>

    <div class="back-motif" role="img" aria-label="Faint scattered music notes decoration"></div>
  </section>

  <section class="spine">
    <span class="spine-text spine-author">Gareth L. Quinby</span>
    <span class="spine-text spine-title">The Stage Performer - a working handbook for launching your trade</span>
  </section>

  <section class="front-cover">
    <div class="rule" style="left:85px; top:0; height:402px;"></div>
    <h1 class="front-title"><span class="lead">the Stage</span><span class="tail">performer</span></h1>
    <p class="front-subtitle">a working handbook<br>for launching your trade</p>
    <div class="cover-art" role="img" aria-label="Silhouette of a head in profile with music notes streaming out as hair"></div>
    <div class="rule" style="left:85px; top:743px; height:142px;"></div>
    <p class="front-author">Gareth L. Quinby</p>
  </section>
</main>
</body>
</html>
```